I need a business card for a new small local scaffolding company. I supply and erect all types of scaffolding for any access need. I thought I could put a safety hat on the Q in NQ to emphasize the 'safe' in KORVELTA. Just a thought.

Industry/Entity Type

Safety

Contact Information for Business Card

KORVELTA NQ , Rob Tenwick , All scaffold & access solutions , Hire , Sales , Transport ,email korveltanq@brisomail.net , 0438710536, fully accredited , abn 47290318854

```html
<!DOCTYPE html>
<html lang="en">
<head>
<meta charset="utf-8">
<title>Korvelta NQ – Business Card</title>
<link rel="stylesheet" href="https://fonts.googleapis.com/css2?family=Mulish:wght@300;400;600;700&display=swap">
<style>
  :root {
    --bg: #d6d6d6;
    --card-white: #ffffff;
    --brand-blue: #35a8de;
    --sky-top: #2b9fd9;
    --sky-bottom: #6cc5ec;
    --scaffold-tint: #bcdcf2;
    --ink: #111111;
    --ink-soft: #333333;
  }
  * { box-sizing: border-box; margin: 0; padding: 0; }
  html, body {
    width: 1200px; height: 1000px; overflow: hidden;
    background: var(--bg);
    font-family: "Mulish", "Helvetica Neue", Arial, sans-serif;
  }
  .card-spread {
    position: absolute; left: 50px; top: 331px;
    width: 1100px; height: 337px;
    display: flex;
    box-shadow: 0 4px 14px rgba(0,0,0,0.18);
  }
  .card { position: relative; width: 550px; height: 337px; overflow: hidden; }
  .card--front { background: var(--card-white); }
  .card--back { background: var(--sky-top); }

  .brand-name {
    font-weight: 300; color: var(--brand-blue); letter-spacing: -0.5px;
    white-space: nowrap;
  }
  .card--front .brand-name {
    position: absolute; right: 37px; top: 44px; font-size: 36px; line-height: 1;
  }
  .tagline {
    position: absolute; right: 37px; top: 92px;
    font-size: 13px; font-weight: 700; color: var(--ink);
  }
  .contact {
    position: absolute; right: 37px; top: 156px; text-align: right;
  }
  .contact__name { font-size: 22px; font-weight: 600; color: var(--ink); line-height: 1.2; }
  .contact__phone {
    font-size: 16px; font-weight: 400; color: var(--ink-soft); margin-top: 2px;
    display: flex; align-items: center; justify-content: flex-end; gap: 5px;
  }
  .contact__phone svg { width: 13px; height: 13px; }
  .contact__email { font-size: 17px; font-weight: 400; color: var(--ink); margin-top: 28px; }
  .contact__accreditation { font-size: 17px; font-weight: 300; color: var(--brand-blue); margin-top: 2px; }

  .scaffold-art {
    position: absolute; left: 0; top: 156px; width: 187px; height: 126px;
    background: linear-gradient(180deg, #e4f1fb 0%, var(--scaffold-tint) 100%);
    opacity: 0.8;
  }

  .sky-photo {
    position: absolute; inset: 0;
    background: linear-gradient(180deg, var(--sky-top) 0%, #47b2e3 55%, var(--sky-bottom) 100%);
  }
  .card--back .brand-name {
    position: absolute; left: 56px; top: 108px;
    font-size: 56px; color: #ffffff; line-height: 1;
  }
</style>
</head>
<body>
  <main class="card-spread">
    <section class="card card--front">
      <div class="scaffold-art" role="img" aria-label="Light blue line drawing of a scaffold frame with planks"></div>
      <div class="brand-name">korveltaNQ</div>
      <p class="tagline">All scaffold &amp; access solutions&nbsp; | Hire | Sales | Transport</p>
      <div class="contact">
        <p class="contact__name">Rob Tenwick</p>
        <p class="contact__phone">
          <svg viewBox="0 0 24 24" aria-hidden="true"><circle cx="12" cy="12" r="11" fill="none" stroke="#333" stroke-width="1.6"/><path d="M8 6.5c-1 1-1 3 .8 5.6 1.8 2.6 4 4.5 5.6 4.6 1 .1 1.8-.6 2-1.3l-2.2-1.6-1.2 1c-1-.5-2.6-2.3-3.1-3.4l1-1.2-1.4-2.3c-.6 0-1.1.2-1.5.6z" fill="#333"/></svg>
          0438 710 536
        </p>
        <p class="contact__email">email: korveltanq@brisomail.net</p>
        <p class="contact__accreditation">fully accredited , abn 47290318854</p>
      </div>
    </section>
    <section class="card card--back">
      <div class="sky-photo" role="img" aria-label="Photo of blue sky with white clouds and a scaffold structure in silhouette"></div>
      <div class="brand-name">korveltaNQ</div>
    </section>
  </main>
</body>
</html>
```